Atendimento nota 11, sem contar a agilidade das pessoas, nos apresentaram diversos modelos e formas de logo. Com certeza iremos indica-lo para outras pessoas.

```html
<!DOCTYPE html>
<html lang="pt-BR">
<head>
<meta charset="utf-8">
<title>Solare Imóveis – Pasta institucional</title>
<link rel="stylesheet" href="https://fonts.googleapis.com/css2?family=Raleway:wght@300;400&display=swap">
<style>
  :root {
    --bg: #e9e9e7;
    --paper: #ffffff;
    --brown: #2b1a10;
    --gold: #c4a465;
    --ink-soft: #8a8a8a;
  }
  html, body {
    margin: 0;
    padding: 0;
    width: 1200px;
    height: 1200px;
    overflow: hidden;
    background: var(--bg);
  }
  .canvas {
    position: relative;
    width: 1200px;
    height: 1200px;
  }
  .folder {
    position: absolute;
    inset: 0;
  }
  .brand-name {
    font-family: "Raleway", sans-serif;
    fill: var(--gold);
  }
  .brand-main { font-weight: 300; font-size: 44px; letter-spacing: 1px; }
  .brand-sub  { font-weight: 300; font-size: 15px; letter-spacing: 9px; }
  .brand-small { font-weight: 400; font-size: 15px; letter-spacing: 1px; }
  .contact-line {
    font-family: "Raleway", sans-serif;
    font-size: 7px;
    fill: var(--ink-soft);
  }
</style>
</head>
<body>
<main class="canvas">
  <svg class="folder" width="1200" height="1200" viewBox="0 0 1200 1200" xmlns="http://www.w3.org/2000/svg">
    <!-- inner left panel -->
    <rect class="panel-left" x="137" y="180" width="463" height="648" fill="var(--paper)"/>
    <!-- cover panel -->
    <rect class="panel-cover" x="600" y="180" width="463" height="648" fill="var(--brown)"/>
    <line class="cover-rule" x1="600" y1="820" x2="1063" y2="820" stroke="var(--gold)" stroke-width="1.5"/>

    <!-- inner pocket -->
    <rect class="pocket-band" x="137" y="828" width="463" height="14" fill="var(--paper)"/>
    <line class="pocket-rule" x1="137" y1="820" x2="600" y2="820" stroke="var(--brown)" stroke-width="1.5"/>
    <path class="pocket-flap" d="M137 842 H600 V942 C540 950 470 965 400 985 C310 1010 220 1030 137 1018 Z" fill="var(--brown)"/>
    <line class="card-slit" x1="384" y1="866" x2="420" y2="846" stroke="#d9d9d9" stroke-width="2"/>
    <line class="card-slit" x1="533" y1="974" x2="578" y2="950" stroke="#d9d9d9" stroke-width="2"/>

    <!-- inner panel signature -->
    <rect class="brand-mark-small" x="359" y="744" width="12" height="12" fill="var(--gold)"/>
    <text class="brand-name brand-small" x="365" y="778" text-anchor="middle">SOLARE</text>
    <text class="contact-line" x="365" y="796" text-anchor="middle">Rua das Acácias, 120 – Centro – Cidade – Estado – (11) 0000-0000</text>
    <text class="contact-line" x="365" y="808" text-anchor="middle">www.solare.com.br – contato@solare.com.br</text>

    <!-- cover brand -->
    <rect class="brand-mark" x="814" y="448" width="28" height="28" fill="var(--gold)"/>
    <text class="brand-name brand-main" x="828" y="548" text-anchor="middle">SOLARE</text>
    <text class="brand-name brand-sub" x="832" y="584" text-anchor="middle">IMÓVEIS</text>
  </svg>
</main>
</body>
</html>
```